Brochure Design For Beauty Salon

We have an existing brochure for our beauty salon business which has been designed in-house.

We need a designer to refresh the look and feel of the brochure, which is intended for print. The print format will be 210mmx210mm (square, stapled).

We need a design for each and every page of the brochure, including the front and back covers.

We are looking for a fresh modern design, quite close to what we already have, but looking more slick and professional.

The primary colors are white, grey and purple. The final design will communicate luxury, prestige and cleanliness and have a heavy focus on creating the feeling of space within each page.

Target Market(s)

Professional Women, aged 20-45

Industry/Entity Type

Beauty Salon

Font styles to use
Sans Serif
Other font styles liked:
• Helvetica

Requirements
Must have
• The project must be ready for print on square paper 210x210mm

```html
<!DOCTYPE html>
<html lang="en">
<head>
<meta charset="utf-8">
<title>Lumi Vale – Treatment Menu</title>
<link rel="stylesheet" href="https://fonts.googleapis.com/css2?family=Roboto:wght@300;400&display=swap">
<style>
  :root {
    --ink: #6f6f6f;
    --ink-copy: #5c5c5c;
    --rule-grey: #b4b4b4;
    --panel-edge: #9a9a9a;
    --purple: #8a0fe0;
    --purple-deep: #7414b4;
    --purple-line: #6a1a9a;
    --lilac: #c9a6e0;
    --paper: #ffffff;
    --accent-red: #e8384f;
    --accent-cyan: #1ec8e0;
    --accent-blue: #3a8fe0;
  }
  * { box-sizing: border-box; margin: 0; padding: 0; }
  html, body {
    width: 1200px; height: 1200px; overflow: hidden;
    background: var(--paper);
    font-family: "Roboto", Helvetica, Arial, sans-serif;
    font-weight: 300;
    color: var(--ink);
  }
  h1, h2, h3 { font-weight: 300; }
  .canvas { position: relative; width: 1200px; height: 1200px; }
  .page {
    position: absolute; overflow: hidden; background: var(--paper);
    border: 1px solid var(--panel-edge);
  }

  /* Front cover */
  .cover { left: 33px; top: 43px; width: 540px; height: 535px; }
  .cover-frame { position: absolute; border: 3px solid var(--purple); }
  .cover-frame--back { left: 41px; top: 18px; width: 479px; height: 487px; }
  .cover-frame--front { left: 23px; top: 32px; width: 478px; height: 488px; border-color: var(--purple-deep); }
  .flower-art {
    position: absolute; left: 262px; top: 212px; width: 278px; height: 323px;
    background: linear-gradient(135deg, #ffffff 0%, #f3f3f3 45%, #e6e6e6 100%);
  }
  .title-box {
    position: absolute; left: 104px; top: 82px; width: 349px; height: 149px;
    border: 2px solid var(--rule-grey); background: var(--paper);
    display: flex; flex-direction: column; align-items: center; justify-content: center;
  }
  .title-box::before {
    content: ""; position: absolute; inset: 5px; border: 1.5px solid var(--rule-grey);
  }
  .brand-name { font-size: 60px; line-height: 1; letter-spacing: 0.5px; color: var(--ink); }
  .brand-sub { font-size: 34px; line-height: 1.1; color: var(--ink); margin-top: 0; }

  /* Back cover / contact */
  .contact-page { left: 618px; top: 43px; width: 531px; height: 532px; }
  .contact-box {
    position: absolute; left: 91px; top: 33px; width: 347px; height: 251px;
    border: 2px solid var(--rule-grey);
  }
  .contact-box::before {
    content: ""; position: absolute; inset: 5px; border: 1.5px solid var(--rule-grey);
  }
  .contact-heading {
    position: absolute; left: 28px; top: 12px; font-size: 32px; letter-spacing: 0.3px; color: var(--ink);
  }
  .contact-line { position: absolute; left: 26px; display: flex; align-items: flex-start; gap: 12px; font-size: 23px; line-height: 27px; color: var(--ink); }
  .contact-line svg { flex: none; width: 26px; height: 26px; }
  .contact-web { top: 63px; }
  .contact-phone { top: 111px; }
  .contact-address { top: 155px; }
  .address-part::before { content: "•"; margin-right: 6px; }
  .spa-art {
    position: absolute; left: 230px; top: 297px; width: 290px; height: 222px;
    background: linear-gradient(180deg, #d9e6e4 0%, #b8d0cf 55%, #cfc3ad 100%);
  }

  /* Inside page */
  .facials-page { left: 33px; top: 623px; width: 540px; height: 539px; border-color: var(--lilac); }
  .hero-photo {
    position: absolute; left: 2px; top: 0; width: 537px; height: 247px;
    background: linear-gradient(180deg, #5b6f9e 0%, #a6b1c8 30%, #e7ddd6 55%, #f4f4f4 100%);
  }
  .section-title {
    position: absolute; left: 184px; top: 286px; padding: 1px 2px;
    border: 1px solid #a78ab8; font-size: 19px; color: var(--ink);
  }
  .body-copy {
    position: absolute; font-size: 8.6px; line-height: 10.8px;
    text-align: center; color: var(--ink-copy);
  }
  .body-copy--intro { left: 145px; top: 319px; width: 250px; }
  .body-copy--treatment { left: 133px; top: 436px; width: 274px; }
  .treatment-row {
    position: absolute; left: 57px; top: 398px; width: 426px;
    display: flex; justify-content: space-between; padding: 0 4px 4px;
    border-bottom: 2px solid var(--purple-line); font-size: 18px; color: var(--ink);
  }
</style>
</head>
<body>
<main class="canvas">

  <section class="page cover" aria-label="Front cover">
    <div class="flower-art" role="img" aria-label="White daisy illustration"></div>
    <div class="cover-frame cover-frame--back"></div>
    <div class="cover-frame cover-frame--front"></div>
    <div class="title-box">
      <h1 class="brand-name">Lumi Vale</h1>
      <p class="brand-sub">Treatment Menu</p>
    </div>
  </section>

  <section class="page contact-page" aria-label="Back cover">
    <div class="contact-box">
      <h2 class="contact-heading">CONTACT</h2>
      <div class="contact-line contact-web">
        <svg viewBox="0 0 26 26" aria-hidden="true"><text x="13" y="20" text-anchor="middle" font-size="24" font-family="Roboto, sans-serif" fill="var(--accent-red)">@</text></svg>
        <span>www.lumivale.co.uk</span>
      </div>
      <div class="contact-line contact-phone">
        <svg viewBox="0 0 26 26" aria-hidden="true">
          <path d="M7 5 l4 0 l1.5 5 l-2.5 2 a12 12 0 0 0 5 5 l2 -2.5 l5 1.5 l0 4 a3 3 0 0 1 -3 3 A17 17 0 0 1 4 8 a3 3 0 0 1 3 -3z" fill="var(--accent-cyan)"/>
          <path d="M15 4 a7 7 0 0 1 7 7 M15 8 a3 3 0 0 1 3 3" stroke="var(--accent-blue)" stroke-width="1.8" fill="none"/>
        </svg>
        <span>020 7946 0321</span>
      </div>
      <div class="contact-line contact-address">
        <svg viewBox="0 0 26 26" aria-hidden="true">
          <path d="M13 2 a8 8 0 0 1 8 8 c0 6 -8 14 -8 14 s-8 -8 -8 -14 a8 8 0 0 1 8 -8z" fill="var(--accent-blue)"/>
          <circle cx="13" cy="10" r="3.5" fill="var(--paper)"/>
        </svg>
        <address style="font-style:normal">
          48 Orchard Row<br>
          <span class="address-part">Elmford Central</span><br>
          <span class="address-part">N7 4QX</span>
        </address>
      </div>
    </div>
    <div class="spa-art" role="img" aria-label="Spa illustration of rolled towels, candles and leafy sprigs"></div>
  </section>

  <section class="page facials-page" aria-label="Facials page">
    <div class="hero-photo" role="img" aria-label="Photo of a client relaxing during a facial massage"></div>
    <h3 class="section-title">Dermaluxe Facials</h3>
    <p class="body-copy body-copy--intro">Every treatment begins with a careful consultation so we can tailor each step to your skin. We cleanse twice, exfoliate gently, clear congestion, then finish with a personalised massage and a calming mask to leave skin bright.</p>
    <div class="treatment-row"><span>Skin Reset</span><span>£10 | 10 mins</span></div>
    <p class="body-copy body-copy--treatment">A quick session with one of our skin therapists. We look closely at your skin, suggest a simple routine that suits it, and show you how to use each product at home.</p>
  </section>

</main>
</body>
</html>
```